Fire Hydrant Repair Parts Flyer

We need a flyer advertising both fire hydrant parts and the manufacturers that we are stocking. Our company is Coastal Flowline Supply and we are a parts distributor who sells directly to contractors. I have attached an example flyer that advertises some other parts we stock. We don't want it to look exactly like the old flyer, but we would like it to be structured similarly. I have also attached a background image for the flyer as well as some pictures of the parts we are stocking. I have also attached pictures of the manufacturer logos that we are stocking. We are trying to convey the parts that we are stocking which are: "Traffic Repair Kits", "Main Valve Repair Kits", "Extension Kits", "Replacement Caps & Gaskets", "Replacement Nozzles", Adjustable Hydrant Wrenches", "Hydrant Diffusers", & "Hydrant Oil". I have attached pictures of some of these items that we would like placed on the flyer. Let me know if you have any questions at all.

```html
<!DOCTYPE html>
<html lang="en">
<head>
<meta charset="utf-8">
<title>Coastal Flowline Supply – Fire Pump Repair Flyer</title>
<link href="https://fonts.googleapis.com/css2?family=Montserrat:wght@400;500;700;800;900&display=swap" rel="stylesheet">
<style>
  :root {
    --stage: #2b2b2b;
    --brand-blue: #3a4fa8;
    --brand-blue-deep: #33479c;
    --brand-red: #e8234e;
    --fire-1: #ffb21e;
    --fire-2: #f25a12;
    --fire-3: #c8160f;
    --paper: #ffffff;
    --panel: #f1f2f5;
    --rule: #dfe2ea;
    --muted: #5c6172;
  }
  * { box-sizing: border-box; margin: 0; padding: 0; }
  html, body { width: 700px; height: 1200px; overflow: hidden; }
  body {
    background: var(--stage);
    font-family: "Montserrat", sans-serif;
    position: relative;
  }
  .flyer {
    position: absolute;
    left: 0; top: 104px;
    width: 700px; height: 991px;
    background: var(--paper);
    overflow: hidden;
  }
  .flyer-backdrop { position: absolute; inset: 0; width: 100%; height: 100%; }

  .brand {
    position: absolute; left: 30px; top: 44px;
    display: flex; align-items: center; gap: 12px;
    z-index: 2;
  }
  .brand-dot { width: 34px; height: 34px; border-radius: 50%; background: var(--brand-red); flex: none; }
  .brand-name {
    font-size: 22px; font-weight: 500; color: var(--brand-blue);
    line-height: 24px; letter-spacing: -0.2px;
  }
  .brand-name span { display: block; }

  .tagline {
    position: absolute; left: 443px; top: 30px; width: 200px;
    text-align: center; color: var(--paper);
    font-weight: 900; font-size: 22px; line-height: 27px; letter-spacing: 0.3px;
  }

  .headline {
    position: absolute; left: 36px; top: 210px;
    font-weight: 900; line-height: 0.95; letter-spacing: -1px;
    background: linear-gradient(180deg, var(--fire-1) 0%, var(--fire-2) 55%, var(--fire-3) 100%);
    -webkit-background-clip: text; background-clip: text; color: transparent;
    filter: drop-shadow(2px 2px 0 #ffffff) drop-shadow(-1px -1px 0 #ffffff) drop-shadow(3px 4px 3px rgba(0,0,0,0.35));
  }
  .headline-top { display: block; font-size: 64px; }
  .headline-bottom { display: block; font-size: 92px; }

  .hydrant-photo {
    position: absolute; left: 446px; top: 92px; width: 218px; height: 522px;
    border-radius: 90px 90px 30px 30px;
    background: linear-gradient(90deg, #b5121e 0%, #ee2b2f 45%, #c41820 100%);
  }

  .parts-list { position: absolute; list-style: none; }
  .parts-list li {
    position: relative; padding-left: 22px;
    color: var(--brand-red); font-weight: 700; font-size: 17px; line-height: 19px;
    margin-bottom: 11px;
  }
  .parts-list li::before {
    content: ""; position: absolute; left: 0; top: 5px;
    width: 11px; height: 11px; border-radius: 50%;
    border: 2.5px solid var(--brand-blue);
  }
  .parts-list.col-a { left: 50px; top: 468px; }
  .parts-list.col-b { left: 213px; top: 468px; }

  .product-strip {
    position: absolute; left: 40px; top: 683px; width: 619px; height: 118px;
    border-radius: 16px; background: var(--panel);
    display: flex; justify-content: space-around; align-items: center; padding: 0 12px;
  }
  .product-photo { width: 82px; height: 82px; border-radius: 10px; }
  .product-photo.cap { background: radial-gradient(circle, #d8323a 0%, #c7c9cf 70%, var(--panel) 100%); }
  .product-photo.kit { background: radial-gradient(circle, #4a4d55 0%, #b9bcc3 70%, var(--panel) 100%); }
  .product-photo.extension { background: radial-gradient(circle, #3c3e44 0%, #aeb1b8 70%, var(--panel) 100%); }
  .product-photo.oil { background: radial-gradient(circle, #f4f4f6 0%, #c9ccd2 70%, var(--panel) 100%); }
  .product-photo.diffuser { background: radial-gradient(circle, #f3b41c 0%, #c8c3b0 70%, var(--panel) 100%); }
  .product-photo.wrench { background: radial-gradient(circle, #9ea3ad 0%, #cfd2d8 70%, var(--panel) 100%); }

  .maker-row {
    position: absolute; left: 40px; top: 801px; width: 619px; height: 102px;
    display: flex;
  }
  .maker {
    display: flex; align-items: center; justify-content: center; gap: 6px;
    padding: 0 6px;
    border-right: 1px solid var(--rule);
    font-size: 10.5px; line-height: 13px; font-weight: 800; color: var(--muted);
    text-transform: uppercase; text-align: left;
  }
  .maker:last-child { border-right: none; }
  .maker-mark { width: 12px; height: 12px; border-radius: 50%; background: var(--muted); flex: none; }
  .maker:nth-child(1) { width: 123px; }
  .maker:nth-child(2) { width: 96px; }
  .maker:nth-child(3) { width: 87px; }
  .maker:nth-child(4) { width: 115px; }
  .maker:nth-child(5) { width: 103px; }
  .maker:nth-child(6) { width: 95px; }

  .footer { position: absolute; left: 0; top: 905px; width: 700px; height: 86px; }
  .footer-bands { position: absolute; inset: 0; width: 100%; height: 100%; }
  .contact { position: absolute; display: flex; align-items: center; gap: 9px; color: var(--paper); }
  .contact svg { flex: none; }
  .contact.phone { left: 42px; top: 12px; font-size: 28px; font-weight: 900; }
  .contact.web { left: 42px; top: 52px; font-size: 16px; font-weight: 500; }
  .contact.address { left: 384px; top: 14px; font-size: 13px; line-height: 16px; font-weight: 500; }
  .contact.email { left: 384px; top: 51px; font-size: 13px; font-weight: 500; }
</style>
</head>
<body>
  <main class="flyer">
    <svg class="flyer-backdrop" viewBox="0 0 859 1216" preserveAspectRatio="none" aria-hidden="true">
      <defs>
        <linearGradient id="band-shade" x1="0" y1="0" x2="0" y2="1">
          <stop offset="0" stop-color="#3d53ad"/>
          <stop offset="1" stop-color="#34489d"/>
        </linearGradient>
      </defs>
      <path d="M494 0 H859 V443 Q620 560 360 520 Q150 490 0 448 V218 Q380 190 494 0 Z" fill="url(#band-shade)"/>
    </svg>

    <header class="brand">
      <span class="brand-dot"></span>
      <span class="brand-name"><span>Coastal Flowline</span><span>Supply</span></span>
    </header>

    <p class="tagline">PARTS AND ACCESSORIES</p>

    <h1 class="headline">
      <span class="headline-top">FIRE PUMP</span>
      <span class="headline-bottom">REPAIR</span>
    </h1>

    <div class="hydrant-photo" role="img" aria-label="Photo of a glossy red fire hydrant with chained caps"></div>

    <ul class="parts-list col-a">
      <li>TRAFFIC<br>REPAIR KITS</li>
      <li>MAIN VALVE<br>REPAIR KITS</li>
      <li>EXTENSION<br>KITS</li>
      <li>HYDRANT<br>DIFFUSERS</li>
    </ul>
    <ul class="parts-list col-b">
      <li>REPLACEMENT<br>CAPS &amp; GASKETS</li>
      <li>REPLACEMENT<br>NOZZLES</li>
      <li>ADJUSTABLE<br>HYDRANT<br>WRENCHES</li>
      <li>HYDRANT OIL</li>
    </ul>

    <section class="product-strip">
      <div class="product-photo cap" role="img" aria-label="Red replacement hydrant cap with chain"></div>
      <div class="product-photo kit" role="img" aria-label="Traffic repair kit with coupling and bolts"></div>
      <div class="product-photo extension" role="img" aria-label="Hydrant extension kit with hardware"></div>
      <div class="product-photo oil" role="img" aria-label="Bottle of hydrant oil"></div>
      <div class="product-photo diffuser" role="img" aria-label="Yellow hydrant diffuser with pressure gauge"></div>
      <div class="product-photo wrench" role="img" aria-label="Adjustable hydrant wrench"></div>
    </section>

    <section class="maker-row">
      <div class="maker"><span class="maker-mark"></span>Ridgeway<br>Flow</div>
      <div class="maker"><span class="maker-mark"></span>Kestrel<br>Valve</div>
      <div class="maker"><span class="maker-mark"></span>Harlan<br>Valve</div>
      <div class="maker"><span class="maker-mark"></span>Ironline<br>Pipe</div>
      <div class="maker"><span class="maker-mark"></span>Brookmont<br>Valve</div>
      <div class="maker"><span class="maker-mark"></span>Delmar<br>Works</div>
    </section>

    <footer class="footer">
      <svg class="footer-bands" viewBox="0 0 700 86" preserveAspectRatio="none" aria-hidden="true">
        <rect width="700" height="86" fill="var(--brand-blue)"/>
        <polygon points="0,0 298,0 370,86 0,86" fill="var(--brand-red)"/>
      </svg>
      <div class="contact phone">
        <svg width="18" height="18" viewBox="0 0 20 20"><circle cx="10" cy="10" r="10" fill="var(--brand-blue)"/><path d="M7 5c.5 0 1.3 1.8 1.3 2.3S7.5 8.3 7.6 8.8c.4 1.3 2.1 3 3.5 3.5.5.1 1-.8 1.5-.8s2.3.8 2.3 1.3-.9 1.9-2 1.9C9.3 14.7 5.3 10.7 5.3 7.1 5.3 6 6.5 5 7 5z" fill="#fff"/></svg>
        <span>(800) 555-0142</span>
      </div>
      <div class="contact web">
        <svg width="17" height="17" viewBox="0 0 20 20"><circle cx="10" cy="10" r="10" fill="var(--brand-blue)"/><circle cx="10" cy="10" r="5.5" fill="none" stroke="#fff" stroke-width="1.3"/><path d="M4.5 10h11M10 4.5c-2.5 3-2.5 8 0 11M10 4.5c2.5 3 2.5 8 0 11" fill="none" stroke="#fff" stroke-width="1.1"/></svg>
        <span>www.coastalflowline.com</span>
      </div>
      <div class="contact address">
        <svg width="18" height="18" viewBox="0 0 20 20"><circle cx="10" cy="10" r="10" fill="var(--brand-red)"/><path d="M10 4a4 4 0 0 1 4 4c0 3-4 7.5-4 7.5S6 11 6 8a4 4 0 0 1 4-4z" fill="#fff"/><circle cx="10" cy="8" r="1.5" fill="var(--brand-red)"/></svg>
        <span>1420 Harbor Point Road<br>Pensacola FL 32502</span>
      </div>
      <div class="contact email">
        <svg width="18" height="18" viewBox="0 0 20 20"><circle cx="10" cy="10" r="10" fill="var(--brand-red)"/><rect x="5" y="6.5" width="10" height="7" rx="1" fill="#fff"/><path d="M5.5 7l4.5 3.5L14.5 7" fill="none" stroke="var(--brand-red)" stroke-width="1.2"/></svg>
        <span>orders@coastalflowline.com</span>
      </div>
    </footer>
  </main>
</body>
</html>
```